Harborline Power Works, LLC New Business Card Design Project

Please do not submit multiple designs that look similar. Many submittals of nearly the same design will result in auto rejection. Please do not submit a design unless you know how to provide a PDF with recognizable text that I can modify and update using Adobe Acrobat. I do not use Adobe Photoshop. Please design a business card using the attached HPW logo. Be creative. Do at least 2-3 different designs. One side should have the logo large with the URL www.HPW-KV.com. The other side of the card should have the name Marcus Pellow. License number 524038. Phone number 860-555-0143. Email service@HPW-KV.com. Physical address 742 Maple Orchard Road, Suite 3, Brightwater, KV. 06099. The company name should also be spelled out somewhere, Harborline Power Works, LLC. Please ensure there is no tiny font. Please also ensure that there is nothing near the edges that might get cut off during printing. It will be 3.5" x 2" horizontal standard business card. I use CardQuarry.com to order. The customer has said they want the business card to use the attached look and color scheme. Please do not submit a design unless you know how to provide a PDF with recognizable text that I can modify and update using Adobe Acrobat. I do not use Adobe Photoshop.
Target Market(s)
Read all instructions above.
Industry/Entity Type
Contact Information for Business Card
Requirements
Must have
- Read all instructions above.
Nice to have
Should not have

```html
<!DOCTYPE html>
<html lang="en">
<head>
<meta charset="utf-8">
<title>Harborline Power Works, LLC — Business Card</title>
<link href="https://fonts.googleapis.com/css2?family=Poppins:wght@500;600;700&display=swap" rel="stylesheet">
<style>
  :root {
    --backdrop: #3a3a3c;
    --card-dark: #111111;
    --card-light: #ffffff;
    --ink-dark: #1a1a1a;
    --ink-light: #ffffff;
  }
  * { margin: 0; padding: 0; box-sizing: border-box; }
  html, body {
    width: 1200px;
    height: 801px;
    overflow: hidden;
    background: var(--backdrop);
    font-family: "Poppins", sans-serif;
  }
  .stage {
    width: 1200px;
    height: 801px;
    display: flex;
    align-items: center;
    justify-content: center;
    gap: 40px;
  }
  .card {
    width: 540px;
    height: 309px;
    border-radius: 22px;
    position: relative;
    box-shadow: 0 10px 28px rgba(0,0,0,0.35);
  }
  .card--front {
    background: var(--card-dark);
    color: var(--ink-light);
    display: flex;
    flex-direction: column;
    align-items: center;
    justify-content: center;
  }
  .brand {
    display: flex;
    align-items: center;
    gap: 18px;
  }
  .brand__dot {
    width: 22px;
    height: 22px;
    border-radius: 50%;
    background: var(--ink-light);
  }
  .brand__name {
    font-weight: 700;
    font-size: 96px;
    line-height: 1;
    letter-spacing: -2px;
  }
  .front__url {
    margin-top: 34px;
    font-weight: 600;
    font-size: 17px;
    letter-spacing: 0.5px;
  }
  .card--back {
    background: var(--card-light);
    color: var(--ink-dark);
    padding: 38px 40px 36px 44px;
  }
  .company {
    font-weight: 700;
    font-size: 25px;
    line-height: 1.2;
  }
  .person {
    margin-top: 30px;
    font-weight: 700;
    font-size: 28px;
    line-height: 1.2;
  }
  .contact {
    margin-top: 10px;
    font-weight: 600;
    font-size: 15px;
    line-height: 1.55;
    letter-spacing: 0.3px;
  }
  .address {
    margin-top: 12px;
    font-weight: 600;
    font-size: 15px;
    line-height: 1.55;
  }
  .license {
    position: absolute;
    right: 40px;
    top: 122px;
    font-weight: 500;
    font-size: 13px;
  }
</style>
</head>
<body>
  <main class="stage">
    <section class="card card--front">
      <div class="brand">
        <span class="brand__dot"></span>
        <span class="brand__name">HPW</span>
      </div>
      <p class="front__url">www.HPW-KV.com</p>
    </section>

    <section class="card card--back">
      <h1 class="company">Harborline Power Works, LLC</h1>
      <h2 class="person">Marcus Pellow</h2>
      <p class="contact">860-555-0143<br>service@HPW-KV.com</p>
      <p class="address">742 Maple Orchard Road, Suite 3<br>Brightwater, KV. 06099</p>
      <p class="license">License number 524038</p>
    </section>
  </main>
</body>
</html>
```